Sales Brochure- Tarven Pugmills

We are in need of a new sales brochure for the construction equipment we sell. The type of equipment is a "Pugmill". I am going to upload a brochure from a different brand that I would like as a "template" and I will upload a handful of photos that I would like to see on the brochure. Just looking to get a rough draft done using which ever pictures you choose from below as the place holders. Then we can revise once we have something to work with. I am open to different template options, and ideally looking for a 1-2 page brochure or a 3-4 page brochure pamphlet. Our company colors are Black and Yellow, I will provide link here to our product page for Pugmills.

https://www.brixholdco.example/pugmills/tarven-portable-pugmill-systems-by-brixholdco/
https://www.brixholdco.example/pugmills/tarven-mini-quillon-pugmill-system/

Target Market(s)

Construction Industry

Industry/Entity Type

Construction Industry

Colors
FFF300
FFF600
FEFA6F
FFFEC7
FFFEE8

Requirements
Must have
• designated area for us to have ability to add text. variety of detailed photos of the Pugmill machines. Must have images named 2 and KT517R from below.
Nice to have
• Please change colors to match our Black and Yellow which you will see on our website, and then follow a template like the one I uploaded.

```html
<!DOCTYPE html>
<html lang="en">
<head>
<meta charset="utf-8">
<title>Tarven Pugmills – Brochure Spreads</title>
<link href="https://fonts.googleapis.com/css2?family=Poppins:wght@400;500;600;700&display=swap" rel="stylesheet">
<style>
  :root{
    --stage:#f2f2f2;
    --paper:#ffffff;
    --ink:#111111;
    --night:#1b1b1b;
    --amber:#f8a01c;
    --mist:#e1e1e1;
    --row-a:#ececec;
    --row-b:#f6f6f6;
    --logo-grey:#9a9a9a;
    --sky:#4f7fcf;
    --earth:#8a7a66;
    --machine:#d99022;
  }
  *{margin:0;padding:0;box-sizing:border-box}
  html,body{width:1200px;height:560px;overflow:hidden}
  body{background:var(--stage);font-family:"Poppins",sans-serif;color:var(--ink);position:relative}
  .page{position:absolute;top:102px;width:253px;height:357px;background:var(--paper);overflow:hidden}
  .page--cover{left:50px}
  .page--intro{left:333px;background:var(--mist)}
  .page--features{left:615px}
  .page--specs{left:898px}
  .abs{position:absolute}
  .photo{position:absolute}
  .photo--site{background:linear-gradient(180deg,var(--sky) 0%,#7ea3de 30%,var(--machine) 55%,var(--earth) 75%,#a79a88 100%)}
  .photo--machine{background:linear-gradient(160deg,#6b8fd1 0%,var(--machine) 45%,#6e5f4e 100%)}
  .photo--detail{background:linear-gradient(180deg,#5a6f66 0%,#3d4b47 100%)}
  .photo--stockpile{background:linear-gradient(180deg,#7fa3e0 0%,#5b5550 60%,#3f3a36 100%)}
  .photo--panel{background:linear-gradient(180deg,#e4a63a 0%,#b77a1e 100%)}

  /* Cover */
  .logo-box{left:18px;top:18px;width:70px;height:27px;background:var(--logo-grey);color:#fff;font-weight:700;font-size:17px;line-height:27px;text-align:center}
  .cover-title{left:18px;top:74px;font-size:22px;font-weight:700;letter-spacing:-.2px;z-index:2}
  .cover-lead{left:18px;top:106px;width:160px;font-size:10px;line-height:12px;z-index:2}
  .cover-url{right:18px;bottom:16px;font-size:5.5px;color:#fff}

  /* Shared type */
  .heading{font-size:14px;font-weight:700;line-height:17px}
  .subheading{font-size:8px;font-weight:500;line-height:10px}
  .body{font-size:5px;line-height:7.3px}
  .light{color:#fff}

  /* Features icons */
  .feature{position:absolute;display:flex;align-items:center;gap:9px;width:110px}
  .feature__icon{width:26px;height:26px;border-radius:50%;background:var(--amber);flex:none;display:flex;align-items:center;justify-content:center}
  .feature__text{font-size:4.8px;line-height:7px}
  .band{left:0;bottom:0;width:100%;height:12px;background:var(--amber)}

  /* Specs */
  .spec-col{position:absolute;top:18px;width:68px}
  .spec-col .photo{position:relative;height:45px;width:68px}
  .spec-col__title{font-size:6.5px;font-weight:500;margin-top:8px}
  .spec-col__text{font-size:4.2px;line-height:6px;margin-top:3px}
  .spec-table{left:18px;top:125px;width:149px;border-collapse:collapse;font-size:4.4px}
  .spec-table caption{background:var(--amber);text-align:left;font-weight:600;font-size:5.5px;padding:2px 4px;height:11px}
  .spec-table th{background:var(--night);color:#fff;text-align:left;font-weight:500;padding:0 4px;height:10px;font-size:5px}
  .spec-table td{padding:0 4px;height:10.4px;color:#555}
  .spec-table tr:nth-child(odd) td{background:var(--row-a)}
  .spec-table tr:nth-child(even) td{background:var(--row-b)}
  .contact{left:0;top:283px;width:110px;height:74px;background:var(--night);padding:12px 18px;color:#fff}
  .contact__title{color:var(--amber);font-size:5.5px;font-weight:600;margin-bottom:4px}
  .contact__line{font-size:3.8px;line-height:5px;display:flex;align-items:center;gap:3px}
  .contact__line svg{width:4px;height:4px;flex:none}
</style>
</head>
<body>

<!-- Cover -->
<section class="page page--cover">
  <div class="abs logo-box">LOGO</div>
  <div class="abs" style="left:0;top:0;width:253px;height:357px;background:var(--amber);clip-path:polygon(114px 58px,253px 18px,253px 200px,114px 200px)"></div>
  <div class="photo photo--site" role="img" aria-label="Yellow portable pugmill plant at a gravel yard under blue sky" style="left:0;top:0;width:253px;height:357px;clip-path:polygon(0 206px,253px 96px,253px 357px,0 357px)"></div>
  <div class="abs" style="left:0;top:0;width:253px;height:357px;background:var(--night);clip-path:polygon(46px 357px,253px 274px,253px 357px)"></div>
  <h1 class="abs cover-title">Brochure Design</h1>
  <p class="abs cover-lead">Lorem ipsum Lorem ipsum dolor sit amet,</p>
  <p class="abs cover-url">www.yourwebsite.com</p>
</section>

<!-- Intro -->
<section class="page page--intro">
  <div class="abs" style="left:0;top:0;width:253px;height:357px;background:var(--amber);clip-path:polygon(0 136px,115px 86px,253px 142px,253px 242px,0 242px)"></div>
  <div class="photo photo--machine" role="img" aria-label="Wheel loader beside a yellow pugmill" style="left:0;top:0;width:253px;height:357px;clip-path:polygon(115px 86px,253px 26px,253px 142px)"></div>
  <div class="photo photo--site" role="img" aria-label="Pugmill plant with loader at a work site" style="left:0;top:242px;width:253px;height:115px"></div>
  <div class="abs" style="left:18px;top:29px;width:112px">
    <h2 class="heading">Heading title</h2>
    <p class="subheading" style="margin-top:3px">Subheading title</p>
    <p class="body" style="margin-top:6px">Lorem ipsum dolor sit amet, consectetuer adipiscing elit, sed diam nonummy nibh euismod tincidunt ut laoreet dolore magna aliquam erat volutpat. Ut wisi enim ad minim veniam, quis nostrud exerci tation ullamcorper suscipit lobortis nisl</p>
  </div>
  <div class="abs" style="left:18px;top:155px;width:220px">
    <h2 class="heading">Heading title</h2>
    <p class="subheading" style="margin-top:3px">Subheading title</p>
    <p class="body" style="margin-top:7px">Lorem ipsum dolor sit amet, consectetuer adipiscing elit, sed diam nonummy nibh euismod tincidunt ut laoreet dolore magna aliquam erat volutpat. Ut wisi enim ad minim veniam, quis nostrud exerci tation ullamcorper suscipit lobortis nisl ut aliquip ex ea commodo consequat. Duis autem vel eum iriure dolor in hendrerit in vulputate velit esse molestie consequat, vel illum dolore eu feugiat nulla facilisis at vero eros et</p>
  </div>
</section>

<!-- Features -->
<section class="page page--features">
  <div class="abs" style="left:0;top:0;width:253px;height:174px;background:var(--night)"></div>
  <div class="photo photo--machine" role="img" aria-label="Trailer-mounted pugmill on a gravel lot" style="left:18px;top:18px;width:100px;height:68px"></div>
  <div class="photo photo--panel" role="img" aria-label="Close-up of the yellow pugmill side panel with product badge" style="left:135px;top:18px;width:100px;height:68px"></div>
  <div class="abs" style="left:18px;top:95px;width:105px">
    <p class="subheading light">Subheading title</p>
    <p class="body light" style="margin-top:6px">Lorem ipsum dolor sit amet, consectetuer adipiscing elit, sed diam nonummy nibh euismod tincidunt ut laoreet dolore magna aliquam erat volutpat. Ut wisi enim ad minim</p>
  </div>
  <div class="abs" style="left:135px;top:95px;width:105px">
    <p class="subheading light">Subheading title</p>
    <p class="body light" style="margin-top:6px">Lorem ipsum dolor sit amet, consectetuer adipiscing elit, sed diam nonummy nibh euismod tincidunt ut laoreet dolore magna aliquam erat volutpat. Ut wisi enim ad minim</p>
  </div>
  <div class="abs" style="left:18px;top:191px;width:225px">
    <h2 class="heading">Heading title</h2>
    <p class="subheading" style="margin-top:2px">Subheading title</p>
    <p class="body" style="margin-top:6px">Lorem ipsum dolor sit amet, consectetuer adipiscing elit, sed diam nonummy nibh euismod tincidunt ut laoreet dolore magna aliquam erat volutpat. Ut wisi enim ad</p>
  </div>
  <div class="feature" style="left:17px;top:255px">
    <span class="feature__icon"><svg width="13" height="13" viewBox="0 0 24 24"><circle cx="12" cy="12" r="7" fill="none" stroke="#111" stroke-width="3" stroke-dasharray="3 2.5"/><circle cx="12" cy="12" r="3" fill="#111"/></svg></span>
    <span class="feature__text">Lorem ipsum dolor sit amet, consectetuer adipiscing elit, sed</span>
  </div>
  <div class="feature" style="left:132px;top:255px">
    <span class="feature__icon"><svg width="13" height="13" viewBox="0 0 24 24"><path d="M4 17a8 8 0 0 1 16 0z" fill="#111"/><rect x="2" y="17" width="20" height="3" fill="#111"/></svg></span>
    <span class="feature__text">Lorem ipsum dolor sit amet, consectetuer adipiscing elit, sed</span>
  </div>
  <div class="feature" style="left:17px;top:293px">
    <span class="feature__icon"><svg width="13" height="13" viewBox="0 0 24 24"><rect x="3" y="7" width="18" height="11" rx="2" fill="#111"/><circle cx="8" cy="12.5" r="2" fill="#f8a01c"/><circle cx="16" cy="12.5" r="2" fill="#f8a01c"/></svg></span>
    <span class="feature__text">Lorem ipsum dolor sit amet, consectetuer adipiscing elit, sed</span>
  </div>
  <div class="feature" style="left:132px;top:293px">
    <span class="feature__icon"><svg width="13" height="13" viewBox="0 0 24 24"><rect x="3" y="4" width="18" height="13" rx="1.5" fill="none" stroke="#111" stroke-width="2.4"/><path d="M9 21h6M12 17v4" stroke="#111" stroke-width="2.4"/><circle cx="12" cy="10.5" r="2.5" fill="#111"/></svg></span>
    <span class="feature__text">Lorem ipsum dolor sit amet, consectetuer adipiscing elit, sed</span>
  </div>
  <div class="abs band"></div>
</section>

<!-- Specs -->
<section class="page page--specs">
  <div class="spec-col" style="left:18px">
    <div class="photo photo--detail" role="img" aria-label="Pugmill control panel with switches and gauges"></div>
    <p class="spec-col__title">Three heading title</p>
    <p class="spec-col__text">Lorem ipsum dolor sit amet, consectetuer adipiscing elit, sed diam nonummy nibh euismod tincidunt ut laoreet</p>
  </div>
  <div class="spec-col" style="left:93px">
    <div class="photo photo--stockpile" role="img" aria-label="Conveyor feeding a material stockpile"></div>
    <p class="spec-col__title">Three heading title</p>
    <p class="spec-col__text">Lorem ipsum dolor sit amet, consectetuer adipiscing elit, sed diam nonummy nibh euismod tincidunt ut laoreet</p>
  </div>
  <div class="spec-col" style="left:166px">
    <div class="photo photo--machine" role="img" aria-label="Close-up of pugmill pump and piping"></div>
    <p class="spec-col__title">Three heading title</p>
    <p class="spec-col__text">Lorem ipsum dolor sit amet, consectetuer adipiscing elit, sed diam nonummy nibh euismod tincidunt ut laoreet</p>
  </div>

  <table class="abs spec-table">
    <caption>Title</caption>
    <thead><tr><th>Title</th><th>Title</th><th>Title</th></tr></thead>
    <tbody>
      <tr><td>123123</td><td>1231313</td><td>123123</td></tr>
      <tr><td>123123</td><td>1231313</td><td>123123</td></tr>
      <tr><td>123123</td><td>1231313</td><td>123123</td></tr>
      <tr><td>123123</td><td>1231313</td><td>123123</td></tr>
      <tr><td>123123</td><td>1231313</td><td>123123</td></tr>
      <tr><td>123123</td><td>1231313</td><td>123123</td></tr>
      <tr><td>123123</td><td>1231313</td><td>123123</td></tr>
    </tbody>
  </table>

  <div class="abs" style="left:18px;top:233px;width:220px">
    <p class="subheading">Subheading title</p>
    <p class="body" style="margin-top:2px">Lorem ipsum dolor sit amet, consectetuer adipiscing elit, sed diam nonummy nibh euismod tincidunt ut laoreet dolore magna aliquam erat volutpat. Ut wisi enim ad</p>
  </div>

  <div class="photo photo--site" role="img" aria-label="Pugmill plant at a quarry site" style="left:0;top:0;width:253px;height:357px;clip-path:polygon(110px 308px,253px 262px,253px 357px,110px 357px)"></div>

  <div class="abs contact">
    <p class="contact__title">Contact us</p>
    <p class="contact__line">218 Calder Rd</p>
    <p class="contact__line">Brookvale</p>
    <p class="contact__line" style="margin-bottom:4px">Ohio</p>
    <p class="contact__line"><svg viewBox="0 0 10 10"><path d="M2 1l2 2-1 1.5a6 6 0 0 0 2.5 2.5L7 6l2 2-1.5 1.5C4 9 1 6 .5 2.5z" fill="#f8a01c"/></svg>(555) 014-2290</p>
    <p class="contact__line"><svg viewBox="0 0 10 10"><rect x="1" y="2" width="8" height="6" fill="none" stroke="#f8a01c" stroke-width="1.2"/><path d="M1 2l4 3 4-3" fill="none" stroke="#f8a01c" stroke-width="1.2"/></svg>info@brixholdco.example</p>
    <p class="contact__line"><svg viewBox="0 0 10 10"><circle cx="5" cy="5" r="4" fill="none" stroke="#f8a01c" stroke-width="1.2"/><path d="M1 5h8M5 1v8" stroke="#f8a01c" stroke-width="1"/></svg>www.yourwebsite</p>
  </div>
</section>

</body>
</html>
```